Book a Belle needs a Stunning web design

Book a Belle is an upmarket agency in Sydney that has lingerie waitresses for events.

Book a Belle is looking for a website design that is as sexy and sophisticated as the ladies who work for them!

The design mustn't be cluttered, tacky or pornographic. What I'm looking for is something better than the industry leader www.velvetgrace.com.au Something classy, sexy and different.

When designing please suggest a CMS, we already use wordpress but are open to suggestions.

We will need a home page that incorporates a feed from a blog and/or social media (please make suggestions and use your discretion as a designer, however we'd like to approve what goes into the feed before it goes in.) The home page could also have a list of our services, but if not we will need a services page. Our Services include:
Lingerie waitressing at events
Lingerie waitresses to help dress the groom pre wedding.
Bucks parties

We have a logo that we'd like incorporated into the design and have attached it.

We will also need a portfolio page for the ladies, This is not to be cluttered, tacky or pornographic. It needs to be classy.

We will also need a "Contact us" page and were thinking that this could potentially also be a "Ask for a quote on your event" page. I.e. have a regular "Contact us" form but have alternate fields if they tick the "I want a quote" box. Alternatively you could have two parts to the contact us page. One that is a regular form and one that has a "Your requirements" box.

Again please use your discretion when designing these, if it's too cluttered it won't work. If it looks tacky, don't do it. If you have suggestions make them.

Target Market(s)

Males between the ages of 18 - 45

Industry/Entity Type

Industry

Requirements
Must have
• Must incorporate our logo.

```html
<!DOCTYPE html>
<html lang="en">
<head>
<meta charset="utf-8">
<title>Book a Belle</title>
<link href="https://fonts.googleapis.com/css2?family=Cinzel:wght@400;700&family=Montserrat:wght@400;600;800&family=Lato:wght@400;700&family=Arimo&display=swap" rel="stylesheet">
<style>
:root{
  --page:#f1f0ef;
  --ink:#2a2326;
  --muted:#4a3d44;
  --pink:#d86fae;
  --pink-dark:#b84d8e;
  --plum:#5a3a52;
  --panel:#ffffff;
  --side:#ededec;
  --rule:#d6d2d2;
  --link:#d27cad;
  --feed-blue:#4aa9d8;
}
*{margin:0;padding:0;box-sizing:border-box}
html,body{width:1165px;height:1200px;overflow:hidden}
body{
  position:relative;
  background:
    radial-gradient(ellipse 230px 420px at 0 470px,#f1dce8 0%,rgba(241,220,232,0) 100%),
    radial-gradient(ellipse 230px 420px at 1165px 470px,#f1dce8 0%,rgba(241,220,232,0) 100%),
    var(--page);
  font-family:"Lato",sans-serif;color:var(--ink);
}
.abs{position:absolute}

.brand{left:136px;top:52px;display:flex;align-items:center;gap:12px}
.brand-name{font-family:"Cinzel",serif;font-weight:700;font-size:30px;color:var(--ink);letter-spacing:1px}
.brand-dot{width:34px;height:34px;border-radius:50%;border:2px solid var(--ink)}

.address{left:899px;top:62px;font-family:"Cinzel",serif;font-size:10px;letter-spacing:1.6px;line-height:17.5px;color:var(--ink);font-style:normal}
.follow{left:776px;top:110px;display:flex;align-items:center;gap:8px}
.follow .sq{width:16px;height:16px;background:#6f88b8}
.follow .sq.alt{background:#61b6e3}
.follow span{font-family:"Arimo",sans-serif;font-size:9.5px;margin-left:6px;letter-spacing:-.2px}

.nav{left:114px;top:153px;width:948px;height:37px;display:flex;
  background:linear-gradient(#e99ac9,var(--pink) 55%,#cf5fa2);border:2px solid #f3b9da}
.nav a{font-family:"Cinzel",serif;font-size:12px;color:#fff;text-decoration:none;
  display:flex;align-items:center;justify-content:center;border-right:1px solid #c35495;box-shadow:1px 0 0 #eea6cf}
.nav a:last-child{border-right:0;box-shadow:none}

.hero{left:115px;top:200px;width:947px;height:423px;background:var(--panel);border:1px solid #e4e1e1}
.services{left:12px;top:9px;width:252px;height:404px;background:linear-gradient(90deg,#e9e9e8,#f4f4f3)}
.services h2{font-family:"Cinzel",serif;font-weight:400;font-size:15px;letter-spacing:3px;text-align:center;margin-top:16px;color:var(--ink)}
.services ul{list-style:none;margin:13px 24px 0}
.services li{border-top:1px solid var(--rule);height:52px;display:flex;align-items:center;justify-content:center;
  text-align:center;font-size:8.5px;font-weight:700;letter-spacing:1.6px;line-height:17.5px;color:var(--muted);white-space:nowrap}
.services li.tall{height:72px}
.services li.wide{letter-spacing:1px;margin:0 -14px;padding:0 14px;border-top:0;box-shadow:inset 0 1px 0 var(--rule)}
.services li.wide{box-shadow:none;background:linear-gradient(var(--rule),var(--rule)) 14px 0/calc(100% - 28px) 1px no-repeat}
.services li.more{font-family:"Cinzel",serif;font-size:11.5px;letter-spacing:2px;text-decoration:underline;font-weight:400}
.photo{top:9px;height:404px}
.ph1{left:276px;width:211px;background:linear-gradient(135deg,#d9d9d9,#8a8a8a 60%,#c4c4c4)}
.ph2{left:487px;width:222px;background:linear-gradient(160deg,#3a3030,#b98b73 45%,#e6d2c2 80%)}
.ph3{left:709px;width:225px;background:linear-gradient(180deg,#3b3b3b,#6b6b6b 50%,#2c2c2c)}
.tag{right:12px;width:290px;font-family:"Montserrat",sans-serif;font-weight:800;color:#fff;text-align:right;padding-right:22px}
.tag-top{top:271px;height:43px;background:rgba(216,111,174,.82);font-size:17px;line-height:45px}
.tag-bottom{top:314px;height:41px;background:rgba(90,58,82,.82);font-size:35px;line-height:38px}

.tile{top:631px;width:306px;height:156px;background:var(--panel);border:1px solid #e4e1e1;padding:7px}
.tile .pic{width:100%;height:100%;position:relative;overflow:hidden}
.t1{left:115px}.t1 .pic{background:linear-gradient(120deg,#6b4a2e,#d9b79b 45%,#8a6136)}
.t2{left:435px}.t2 .pic{background:linear-gradient(100deg,#3d2a22,#9b7560 50%,#4b3429)}
.t3{left:756px}.t3 .pic{background:linear-gradient(135deg,#e6e3dc,#d6d2c8)}
.label{position:absolute;font-family:"Montserrat",sans-serif;font-weight:800;color:#fff;text-align:center}
.lbl-up{left:20px;top:72px;width:244px;height:32px;background:rgba(90,58,82,.85);font-size:17px;line-height:32px}
.lbl-up2{left:20px;top:104px;width:244px;height:33px;background:rgba(216,111,174,.75);font-weight:400;font-size:17px;line-height:28px;color:#fbe9f3}
.lbl-gal{left:26px;top:99px;width:240px;height:32px;background:rgba(90,58,82,.8);font-size:17px;line-height:32px}
.lbl-find{left:27px;top:100px;width:245px;height:32px;background:rgba(90,58,82,.85);font-size:17px;line-height:32px}

.feed{left:115px;top:818px;width:947px;height:133px;background:var(--panel);border:1px solid #e4e1e1}
.feed-inner{position:absolute;inset:4px;border:1px solid #e4e1e1}
.feed-name{position:absolute;left:45px;top:16px;font-family:"Montserrat",sans-serif;font-weight:600;font-size:19px;color:var(--feed-blue)}
.post{position:absolute;top:53px;width:420px;font-family:"Arimo",sans-serif;font-size:13.5px;line-height:17.5px;color:#3a3a3a}
.post a{color:var(--link)}
.post .mention{color:var(--link);text-decoration:none}
.post .actions{font-size:11.5px;color:var(--feed-blue);margin-top:1px;display:flex;gap:14px}
.p1{left:45px}.p2{left:494px}

.foot-rule{left:120px;top:994px;width:934px;height:1px;background:#c9c5c5}
.foot-nav{top:1012px;font-family:"Cinzel",serif;font-size:11.5px;color:var(--ink)}
.cities{left:0;width:1165px;top:1058px;text-align:center;font-family:"Cinzel",serif;font-size:10.5px;color:var(--ink);word-spacing:2px}
.cities span{margin:0 12px}
.foot-brand{left:0;width:1165px;top:1118px;display:flex;justify-content:center;align-items:center;gap:10px}
.foot-brand .brand-name{font-size:24px}
.foot-brand .brand-dot{width:28px;height:28px}
</style>
</head>
<body>
<header>
  <div class="abs brand"><span class="brand-name">Book a Belle</span><span class="brand-dot"></span></div>
  <div class="abs follow"><i class="sq"></i><i class="sq alt"></i><span>FOLLOW US</span></div>
  <address class="abs address">5/F LAUREL HOUSE<br>22-24 HARBOUR LANE<br>CENTRAL, GOLD COAST<br>MAYA TORRENS</address>
</header>

<nav class="abs nav">
  <a style="width:127px">Home</a><a style="width:184px">Services</a><a style="width:158px">Girls Gallery</a><a style="width:139px">What we do</a><a style="width:169px">About us</a><a style="width:167px">Contact Us</a>
</nav>

<section class="abs hero">
  <div class="abs services">
    <h2>SERVICES</h2>
    <ul>
      <li class="tall">LINGERIE WAITRESSING<br>AT EVENTS</li>
      <li class="tall wide">LINGERIE WAITRESSES TO HELP DRESS<br>THE GROOM PRE WEDDING.</li>
      <li>BUCKS PARTIES</li>
      <li>PARTY BUS TOURS</li>
      <li>TOPLESS POKER</li>
      <li class="more">VIEW FULL LIST</li>
    </ul>
  </div>
  <div class="abs photo ph1" role="img" aria-label="Black and white portrait of a model in lingerie"></div>
  <div class="abs photo ph2" role="img" aria-label="Colour photo of a model in white lace lingerie"></div>
  <div class="abs photo ph3" role="img" aria-label="Black and white photo of a model in a lace slip"></div>
  <div class="abs tag tag-top">PRETTIEST GIRLS FOR YOUR</div>
  <div class="abs tag tag-bottom">EVENTS</div>
</section>

<div class="abs tile t1"><div class="pic" role="img" aria-label="Model reclining beside candles in a gilded room">
  <div class="label lbl-up">UPCOMING SHOWS</div><div class="label lbl-up2">IN NOVEMBER</div></div></div>
<div class="abs tile t2"><div class="pic" role="img" aria-label="Group of men enjoying a show">
  <div class="label lbl-gal">VIEW SHOWS GALLERY</div></div></div>
<div class="abs tile t3"><div class="pic" role="img" aria-label="Street map showing the agency location">
  <div class="label lbl-find">FIND US</div></div></div>

<section class="abs feed">
  <div class="feed-inner">
    <div class="feed-name">Feedline</div>
    <div class="post p1">A tribute to all the cool girls courtesy of <a class="mention">@velourmag</a> - shot by Oren Castell starring Lena Varga,Noemi... <a>vg.link/8t41Qx2k</a>
      <div class="actions"><span>Expand</span><span>&#8630; Reply</span><span>&#8645; Retweet</span><span>&#9733; Favorite</span></div></div>
    <div class="post p2">A tribute to all the cool girls courtesy of <a class="mention">@velourmag</a> - shot by Oren Castell starring Lena Varga,Noemi... <a>vg.link/8t41Qx2k</a>
      <div class="actions"><span>Expand</span><span>&#8630; Reply</span><span>&#8645; Retweet</span><span>&#9733; Favorite</span></div></div>
  </div>
</section>

<footer>
  <div class="abs foot-rule"></div>
  <span class="abs foot-nav" style="left:169px">Home</span>
  <span class="abs foot-nav" style="left:305px">Services</span>
  <span class="abs foot-nav" style="left:444px">Girls Gallery</span>
  <span class="abs foot-nav" style="left:584px">What we do</span>
  <span class="abs foot-nav" style="left:731px">About us</span>
  <span class="abs foot-nav" style="left:878px">Contact Us</span>
  <div class="abs cities"><span>SYDNEY</span>-<span>MELBOURNE</span>-<span>BRISBANE</span>-<span>GOLD COAST</span></div>
  <div class="abs foot-brand"><span class="brand-name">Book a Belle</span><span class="brand-dot"></span></div>
</footer>
</body>
</html>
```